New Web Site Design - Ironwood Signal Solutions

We are looking for a completely new web site design. Ironwood Signal Solutions is a full service company providing PBX and IP/Cloud Based phone systems. We also sell and install video camera surveillance systems and provide low voltage cabling services (CAT5 and CAT3). We are looking for something professional looking. We want to be able to showcase our vendor partners as well as be able to show photos of some of the work we have done. We will also want to be able to post PDF brochures as well as make changes to the website ourselves.

Target Market(s)

Commercial

Industry/Entity Type

Communication

Coding

Coded - Design and coding required

Number of Pages Required

5+ page

Font styles to use
Sans Serif

Colors
0455a3

Requirements
Must have
• Ability to upload PDF brochures
• Professional look and feel
• Ability to upload and easily insert job photos
• Thinking it should have at least 6 pages: Main page, phone systems and services page, carrier services page, video surveillance systems and service page, low voltage cabling services page, contact us page

```html
<!DOCTYPE html>
<html lang="en">
<head>
<meta charset="utf-8">
<title>Ironwood Signal Solutions</title>
<link href="https://fonts.googleapis.com/css2?family=Roboto:wght@400;500;700&family=Roboto+Condensed:wght@400;700&family=Roboto+Slab:wght@400&display=swap" rel="stylesheet">
<style>
:root{
  --brand:#0455a3;
  --brand-dark:#033f7a;
  --ink:#222;
  --text:#444;
  --muted:#666;
  --line:#d6d6d6;
  --band:#efefef;
  --footer:#3c3c3c;
  --footer-deep:#2b2b2b;
  --white:#fff;
}
*{box-sizing:border-box;margin:0;padding:0}
html,body{width:1200px;height:2679px;overflow:hidden;background:var(--white)}
body{font-family:"Roboto",Arial,sans-serif;color:var(--text);position:relative}
.abs{position:absolute}
h2.section-title{font-family:"Roboto Condensed",sans-serif;font-weight:400;font-size:29px;color:var(--ink);text-align:center}
.title-rule{width:730px;height:1px;background:var(--line);margin:0 auto;position:relative}
.title-rule::after{content:"";position:absolute;left:50%;top:-1px;width:70px;height:3px;margin-left:-35px;background:var(--brand)}
.read-more{color:var(--brand);text-decoration:underline;font-size:13px}

/* header */
.site-header{left:0;top:0;width:1200px;height:143px;background:var(--white)}
.header-edge-left{left:0;top:0;width:80px;height:143px;background:var(--brand)}
.header-edge-right{left:1115px;top:0;width:85px;height:143px;background:var(--brand)}
.logo{left:82px;top:30px;display:flex;align-items:center;gap:10px}
.logo-mark{width:86px;height:86px;border-radius:50%;background:var(--brand-dark);border:4px solid var(--white);margin-left:-8px}
.logo-name{font-family:"Roboto",sans-serif;font-size:30px;font-weight:500;color:var(--brand);line-height:1}
.logo-sub{display:block;font-size:14px;font-weight:400;letter-spacing:.5px;color:var(--brand);margin-top:4px}
.follow{left:893px;top:20px;display:flex;align-items:center;gap:8px;font-size:13px;color:#333}
.follow span.dot{width:30px;height:30px;border-radius:50%;background:#333}
.brochure{left:686px;top:74px;display:flex;align-items:center}
.brochure-icon{width:44px;height:50px;border:2px solid var(--brand);background:var(--white)}
.brochure-btn{background:var(--brand);color:var(--white);font-size:15px;padding:7px 16px;margin-left:-2px}
.call{left:938px;top:78px;display:flex;gap:8px;align-items:center}
.call-text{font-size:14px;color:#333;line-height:1.2}
.call-text strong{display:block;font-size:21px;font-weight:400;color:var(--brand)}

/* nav */
.main-nav{left:0;top:145px;width:1200px;height:48px;background:var(--brand);display:flex;align-items:center;padding-left:74px;gap:0}
.main-nav a{font-family:"Roboto Slab",serif;color:var(--white);font-size:15px;text-decoration:none;padding:0 26px;height:48px;line-height:48px;border-right:1px solid rgba(255,255,255,.25)}
.main-nav a:first-child{padding-left:20px}
.main-nav a:last-child{border-right:none}

/* hero */
.hero{left:0;top:193px;width:1200px;height:449px;background:linear-gradient(100deg,#a9bccb 0%,#c9d7e1 40%,#8ea6b9 75%,#3e4f60 100%)}
.hero h1{position:absolute;left:95px;top:130px;font-family:"Roboto Condensed",sans-serif;font-weight:400;font-size:41px;line-height:61px;color:var(--white)}
.hero-arrow{position:absolute;top:206px;width:38px;height:34px;background:#444;display:flex;align-items:center;justify-content:center}

/* products */
.products{left:0;top:670px;width:1200px}
.products .intro{text-align:center;font-size:13px;color:#333;margin:10px 0 8px}
.service-row{display:flex;justify-content:center;gap:18px;margin-top:30px}
.service{width:205px;text-align:center}
.service-icon{width:118px;height:118px;margin:0 auto;border-radius:50%;border:3px solid var(--brand);padding:5px}
.service-icon div{width:100%;height:100%;border-radius:50%;background:var(--brand);display:flex;align-items:center;justify-content:center}
.service h3{font-family:"Roboto Condensed",sans-serif;font-weight:400;font-size:18px;color:#222;margin:16px 0 12px}
.service p{font-size:12.5px;color:var(--muted);line-height:17px;margin-bottom:14px}

/* welcome */
.welcome{left:105px;top:1110px;width:990px;text-align:center}
.welcome p{font-size:12.8px;line-height:20px;color:#333;margin:22px 0 6px}
.welcome-shadow{left:95px;top:1318px;width:1010px;height:10px;background:radial-gradient(ellipse at top,rgba(0,0,0,.12),transparent 70%)}

/* gallery */
.gallery{left:0;top:1352px;width:1200px}
.gallery-row{display:flex;justify-content:center;gap:14px;margin-top:26px}
.gallery-item{width:248px;height:230px;border:4px solid #d7d7d7;position:relative;overflow:hidden}
.gallery-item .photo{width:100%;height:100%}
.gallery-item span{position:absolute;left:0;bottom:0;width:100%;height:44px;background:rgba(0,0,0,.75);color:var(--white);font-family:"Roboto Condensed",sans-serif;font-size:18px;text-align:center;line-height:44px}
.pager{display:flex;justify-content:center;gap:10px;margin-top:22px}
.pager span{width:26px;height:22px;border:1px solid #888;display:flex;align-items:center;justify-content:center}

/* reviews */
.reviews{left:0;top:1733px;width:1200px;height:320px;background:var(--band)}
.reviews h2{margin-top:38px}
.reviews .title-rule{width:200px;margin-top:10px}
.review-client{position:absolute;left:113px;top:138px;width:170px;height:74px;border:2px solid var(--brand);border-radius:6px;background:var(--white);display:flex;align-items:center;justify-content:center;font-size:22px;font-weight:700;color:#333}
.review-quote{position:absolute;left:310px;top:150px;width:760px;font-size:12.6px;font-style:italic;line-height:21px;color:#333;padding-left:36px}
.review-quote::before{content:"\201C";position:absolute;left:0;top:-18px;font-size:60px;color:#ccc;font-style:normal;font-family:Georgia,serif}
.review-by{position:absolute;left:314px;top:290px;font-size:13px;color:var(--brand)}
.review-by strong{font-weight:700}
.side-arrow{position:absolute;top:0;width:14px;height:24px}

/* partners */
.partners{left:0;top:2075px;width:1200px}
.partners .title-rule{width:230px;margin-top:10px}
.partner-row{display:flex;justify-content:center;gap:22px;margin-top:36px;position:relative}
.partner{width:154px;height:74px;border:1px solid #ccc;border-radius:3px;background:var(--white);display:flex;align-items:center;justify-content:center}
.partner div{width:100px;height:36px;border-radius:3px}

/* footer */
.site-footer{left:0;top:2280px;width:1200px;height:360px;background:linear-gradient(180deg,#4a4a4a,#333)}
.footer-map{position:absolute;inset:0;background:linear-gradient(135deg,rgba(255,255,255,.05),rgba(0,0,0,.08))}
.contact{position:absolute;left:100px;top:20px;width:340px;color:#eee}
.contact h4{font-size:18px;font-weight:400;padding-bottom:10px;border-bottom:1px dashed #777;margin-bottom:14px}
.contact-item{display:flex;gap:16px;margin-bottom:17px;font-size:13px;line-height:18px}
.contact-item svg{flex:none;margin-top:2px}
.footer-brand{position:absolute;left:500px;top:95px;color:#9aa3ad;font-size:22px;line-height:1.2}
.footer-brand .ring{width:102px;height:102px;border-radius:50%;border:2px solid #9aa3ad;margin-bottom:10px}
.footer-brand small{display:block;font-size:14px}
.inquiry{position:absolute;left:773px;top:20px;width:312px;height:326px;background:rgba(110,110,110,.75);padding:16px 14px}
.inquiry h4{display:flex;align-items:center;gap:12px;color:var(--white);font-size:22px;font-weight:400}
.inquiry .phone-dot{width:40px;height:40px;border-radius:50%;background:var(--white);display:flex;align-items:center;justify-content:center}
.inquiry p{color:#eee;font-size:12.5px;margin:16px 0 12px}
.inquiry .field{height:32px;background:rgba(255,255,255,.12);border-bottom:1px solid rgba(255,255,255,.2);color:#ddd;font-size:12px;padding:9px 12px;margin-bottom:4px}
.inquiry .field.tall{height:56px}
.inquiry .submit{display:inline-block;margin-top:12px;background:var(--brand);color:var(--white);font-weight:700;font-size:15px;padding:7px 28px}
.copyright{left:0;top:2640px;width:1200px;height:39px;background:var(--footer-deep);color:#ddd;font-size:12px;text-align:center;line-height:39px}
</style>
</head>
<body>

<header class="abs site-header">
  <div class="abs header-edge-left"></div>
  <div class="abs header-edge-right"></div>
  <div class="abs logo">
    <div class="logo-mark"></div>
    <div class="logo-name">Ironwood Signal<span class="logo-sub">IRONWOOD SIGNAL SOLUTIONS</span></div>
  </div>
  <div class="abs follow">Follow Us On <span class="dot"></span><span class="dot"></span><span class="dot"></span></div>
  <div class="abs brochure">
    <div class="brochure-icon"></div>
    <div class="brochure-btn">Download Our Brochure</div>
  </div>
  <div class="abs call">
    <svg width="26" height="26" viewBox="0 0 24 24"><circle cx="12" cy="12" r="11" fill="none" stroke="#0455a3" stroke-width="1.5"/><path d="M8 6c1 0 2 2 2 3s-1 1-1 2 2 4 4 4 1-1 2-1 3 1 3 2-1 2-2 2C11 18 6 13 6 8c0-1 1-2 2-2z" fill="#0455a3"/></svg>
    <div class="call-text">Call Us Today<strong>555-014-2290</strong></div>
  </div>
</header>

<nav class="abs main-nav">
  <a>About Us</a><a>Phone Systems &amp; Services</a><a>Low Voltage Cabling Service</a><a>Carrier Services</a><a>Video Surveillance Systems Service</a>
</nav>

<section class="abs hero" role="img" aria-label="Business person touching a cloud network diagram linking firewall, reports, fax, email, contacts and voicemail">
  <h1>Hosted PBX<br>The Business Phone<br>System in the Cloud</h1>
  <div class="hero-arrow" style="left:0"><svg width="12" height="14"><path d="M9 1L3 7l6 6" stroke="#fff" stroke-width="2" fill="none"/></svg></div>
  <div class="hero-arrow" style="right:0"><svg width="12" height="14"><path d="M3 1l6 6-6 6" stroke="#fff" stroke-width="2" fill="none"/></svg></div>
</section>

<section class="abs products">
  <h2 class="section-title">Product &amp; Services</h2>
  <p class="intro">Lorem ipsum dolor sit amet, consectetur adipiscing elit. Aenean et dignissim sem, &nbsp;interdum risus. Vestibulum consectetur</p>
  <div class="title-rule"></div>
  <div class="service-row">
    <div class="service">
      <div class="service-icon"><div><svg width="50" height="50" viewBox="0 0 50 50"><rect x="8" y="14" width="34" height="26" rx="2" fill="none" stroke="#fff" stroke-width="2.5"/><rect x="12" y="8" width="9" height="34" rx="2" fill="#fff"/><rect x="26" y="18" width="12" height="5" fill="#fff"/><rect x="26" y="27" width="12" height="9" fill="#fff"/></svg></div></div>
      <h3>PBX Phone Systems</h3>
      <p>Lorem ipsum dolr sit amet, consectetur adipiscing elit. Aenean et dign.</p>
      <a class="read-more">Read more</a>
    </div>
    <div class="service">
      <div class="service-icon"><div><svg width="54" height="44" viewBox="0 0 54 44"><path d="M14 34a10 10 0 0 1 0-20 14 14 0 0 1 27 3 8 8 0 0 1 0 17z" fill="none" stroke="#fff" stroke-width="2.5"/><rect x="20" y="20" width="14" height="9" rx="2" fill="#fff"/></svg></div></div>
      <h3>IP/Cloud Phone System</h3>
      <p>Lorem ipsum dolr sit amet, consectetur adipiscing elit. Aenean et dign.</p>
      <a class="read-more">Read more</a>
    </div>
    <div class="service">
      <div class="service-icon"><div><svg width="54" height="44" viewBox="0 0 54 44"><rect x="6" y="10" width="34" height="14" rx="3" transform="rotate(15 23 17)" fill="#fff"/><rect x="20" y="26" width="4" height="12" fill="#fff"/><rect x="10" y="36" width="18" height="4" fill="#fff"/><rect x="40" y="16" width="8" height="8" fill="#fff"/></svg></div></div>
      <h3>Video Camera Surveillance</h3>
      <p>Lorem ipsum dolr sit amet, consectetur adipiscing elit. Aenean et dign.</p>
      <a class="read-more">Read more</a>
    </div>
    <div class="service">
      <div class="service-icon"><div><svg width="44" height="50" viewBox="0 0 44 50"><rect x="14" y="12" width="16" height="30" rx="3" fill="none" stroke="#fff" stroke-width="2.5"/><circle cx="22" cy="36" r="2" fill="#fff"/><path d="M8 14a18 18 0 0 1 28 0M12 18a12 12 0 0 1 20 0" stroke="#fff" stroke-width="2" fill="none"/></svg></div></div>
      <h3>Carrier Service</h3>
      <p>Lorem ipsum dolr sit amet, consectetur adipiscing elit. Aenean et dign.</p>
      <a class="read-more">Read more</a>
    </div>
    <div class="service">
      <div class="service-icon"><div><svg width="50" height="50" viewBox="0 0 50 50"><path d="M8 40c10 0 8-14 18-14s10 10 16 4" stroke="#fff" stroke-width="3" fill="none"/><rect x="30" y="8" width="10" height="16" rx="2" transform="rotate(30 35 16)" fill="#fff"/></svg></div></div>
      <h3>Low Voltage Cabling</h3>
      <p>Lorem ipsum dolr sit amet, consectetur adipiscing elit. Aenean et dign.</p>
      <a class="read-more">Read more</a>
    </div>
  </div>
</section>

<section class="abs welcome">
  <h2 class="section-title">Welcome to Ironwood Signal Solutions</h2>
  <p>Ironwood Signal is a communications company based in Phoenix, providing a host of services to customers of all sizes, industries, and professions. We pride ourselves on having a great professional relationship with each of our clients. This allows us to truly understand our customer's needs. Our key service concept is to relieve the customer of any worries relating to telecom/IT by reducing their over-all costs, and provide a reliable and comprehensive communication solution. Our team has worked together for nearly 10 years and is cohesive in our approach in exceeding our customer's expectations.</p>
  <a class="read-more">Read more</a>
</section>
<div class="abs welcome-shadow"></div>

<section class="abs gallery">
  <h2 class="section-title">Project Gallery</h2>
  <div class="title-rule" style="width:200px;margin-top:10px"></div>
  <div class="gallery-row">
    <div class="gallery-item"><div class="photo" role="img" aria-label="Desk phone handset on a white desk" style="background:linear-gradient(160deg,#f2f2f2,#9a9a9a 70%,#333)"></div><span>Lorem Ispim is Dummmy</span></div>
    <div class="gallery-item"><div class="photo" role="img" aria-label="Technician installing a security camera under blue sky" style="background:linear-gradient(160deg,#4a7fb8,#6a93c0 50%,#8a6a5a)"></div><span>Lorem Ispim is Dummmy</span></div>
    <div class="gallery-item"><div class="photo" role="img" aria-label="Cabling technician in hard hat holding cable" style="background:linear-gradient(160deg,#e6e8ea,#c7a184 45%,#2d3e5a)"></div><span>Lorem Ispim is Dummmy</span></div>
    <div class="gallery-item"><div class="photo" role="img" aria-label="Hands using an office IP phone" style="background:linear-gradient(160deg,#eef2f5,#b0b8bf 50%,#2e2e2e)"></div><span>Lorem Ispim is Dummmy</span></div>
  </div>
  <div class="pager">
    <span><svg width="8" height="12"><path d="M7 1L2 6l5 5" stroke="#333" stroke-width="1.6" fill="none"/></svg></span>
    <span style="border-color:var(--brand)"><svg width="8" height="12"><path d="M1 1l5 5-5 5" stroke="#0455a3" stroke-width="1.6" fill="none"/></svg></span>
  </div>
</section>

<section class="abs reviews">
  <h2 class="section-title">Customer Reviews</h2>
  <div class="title-rule"></div>
  <svg class="side-arrow" style="left:70px;top:158px" viewBox="0 0 14 24"><path d="M12 2L3 12l9 10" stroke="#777" stroke-width="2" fill="none"/></svg>
  <svg class="side-arrow" style="left:1126px;top:158px" viewBox="0 0 14 24"><path d="M2 2l9 10-9 10" stroke="#777" stroke-width="2" fill="none"/></svg>
  <div class="review-client">Harbor Table</div>
  <p class="review-quote">Ironwood Signal has been and invaluable partner and an extension of our team since day 1 at Harbor Table. They truly are that mythical, rare breed of vendor that excel at planning, execution, communication, pricing, support, training – the entire package. Navigating hyper growth on a national scale can be daunting. Ironwood Signal has been with us every step of the way and delivered on budget, on time - every time. Their support and solutions are the backbone of our telecommunications infrastructure, and have contributed greatly to our success. I cannot recommend Marcus and his team highly enough!</p>
  <div class="review-by"><strong>Dana Whitfield,</strong> &nbsp;Chief Information Officer | Harbor Group</div>
</section>

<section class="abs partners">
  <h2 class="section-title">Our Vending Partners</h2>
  <div class="title-rule"></div>
  <div class="partner-row">
    <svg class="side-arrow" style="left:70px;top:24px" viewBox="0 0 14 24"><path d="M12 2L3 12l9 10" stroke="#777" stroke-width="2" fill="none"/></svg>
    <div class="partner"><div style="background:#c9a46a;width:50px;border-radius:50%;height:50px"></div></div>
    <div class="partner"><div style="background:#e3261d"></div></div>
    <div class="partner"><div style="background:#1c5aa6"></div></div>
    <div class="partner"><div style="background:#7ab51d"></div></div>
    <div class="partner"><div style="background:#1a8a3a"></div></div>
    <div class="partner"><div style="background:#222;height:24px"></div></div>
    <svg class="side-arrow" style="left:1126px;top:24px" viewBox="0 0 14 24"><path d="M2 2l9 10-9 10" stroke="#777" stroke-width="2" fill="none"/></svg>
  </div>
</section>

<footer class="abs site-footer">
  <div class="footer-map" role="img" aria-label="Faded street map of the office area"></div>
  <div class="contact">
    <h4>Contact Details</h4>
    <div class="contact-item"><svg width="14" height="18" viewBox="0 0 14 18"><path d="M7 0a7 7 0 0 1 7 7c0 5-7 11-7 11S0 12 0 7a7 7 0 0 1 7-7z" fill="#fff"/><circle cx="7" cy="7" r="2.5" fill="#444"/></svg><div>Postal Address<br>Street Name, City Name State Zipcode</div></div>
    <div class="contact-item"><svg width="14" height="16" viewBox="0 0 24 24"><path d="M6 2c2 0 4 4 4 5s-2 2-2 3 3 6 6 6 2-2 3-2 5 2 5 4-2 4-4 4C9 22 2 15 2 6c0-2 2-4 4-4z" fill="#fff"/></svg><div>Telephone<br>555-014-2290 &amp; Fax: 555-014-2291</div></div>
    <div class="contact-item"><svg width="14" height="12" viewBox="0 0 14 12"><rect width="14" height="12" fill="#fff"/><path d="M0 0l7 6 7-6" stroke="#444" fill="none"/></svg><div>Email<br>Information and Support: inquiry@ironwoodsignal.com</div></div>
    <div class="contact-item"><svg width="14" height="14"><rect width="14" height="14" fill="#fff"/></svg><div>Social<br>www.social-one.com/ironwoodsignal</div></div>
    <div class="contact-item"><svg width="14" height="14"><rect width="14" height="14" rx="3" fill="#fff"/></svg><div>Social<br>www.social-two.com/ironwoodsignal</div></div>
  </div>
  <div class="footer-brand"><div class="ring"></div>Ironwood Signal<small>IRONWOOD SIGNAL SOLUTIONS</small></div>
  <div class="inquiry">
    <h4><span class="phone-dot"><svg width="20" height="20" viewBox="0 0 24 24"><path d="M6 2c2 0 4 4 4 5s-2 2-2 3 3 6 6 6 2-2 3-2 5 2 5 4-2 4-4 4C9 22 2 15 2 6c0-2 2-4 4-4z" fill="#0455a3"/></svg></span>Quick Inquiry</h4>
    <p>Lorem ipsum dolor sit amet, consectetuer</p>
    <div class="field">Name</div>
    <div class="field">Email</div>
    <div class="field">Phone</div>
    <div class="field tall">Message</div>
    <span class="submit">SUBMIT</span>
  </div>
</footer>
<div class="abs copyright">Copyright© 2016 &nbsp;Ironwood Signal Solutions &nbsp;All Rights Reserved</div>

</body>
</html>
```